Need Edgy Web Design Home Page for Entertainment Agency

We need a web design splash page for our entertainment company, Velvet Crown Agency based (Los Angeles and New York).
Velvet Crown is a full service PR, marketing and special events agency based in Los Angeles and New York. We aim to serve the most elite in entertainment, media and sports.

With a combined experience of over 30 years in the entertainment industry, our team is committed to deliver each client with the upmost service and contemporary strategies to increase your business objective.

CREATIVE, EDGY & TRENDSETTING

SERVICES

PR Campaigns

Media Relations

Talent Representation

Brand Marketing & Activations

Special Events: Publicity & Consulting

EXPERTISE

Television

Film

Talent

Music

Marketing & Promotions

Industry Events

Digital & Social Media

Looking for a home page that is flashy, edgy and creative. I've provided our logos and contact details:

Delia Varga
dvarga@velcrowmla.com

Jonah Pryce
jpryce@velcrowmny.com

Renata Olmos
rolmos@velcrowmla.com

Target Market(s)

Los Angeles and New York

Industry/Entity Type

Entertainment

Number of Pages Required

1 page

Font styles to use
Serif
Decorative

Requirements
Must have
• 1. Logo
• 2. Description of services but done creatively
• 4. Visuals (Stock images: cool edgy millennials & graphics images that make sense for our agency)
• 5. Contact Details
• Reference: https://www.tunelatchery.net & http://www.thekestrelworks.com
Nice to have
• If possible would love to have stock cartoon images included as images of Delia and I. Reference image (http://www.pixmarrowfield.com/pic-507314862/stock-vector-cute-cartoon-characters-young-boy-and-girl-in-cool-casual-outfits.html)
Should not have
• Should not look boring!

```html
<!DOCTYPE html>
<html lang="en">
<head>
<meta charset="utf-8">
<title>Velvet Crown Agency</title>
<link rel="stylesheet" href="https://fonts.googleapis.com/css2?family=Oswald:wght@400;500&family=Roboto:wght@400;500;700&display=swap">
<style>
:root{
  --ink:#1c1c1c;
  --ink-soft:#262a2c;
  --bar:#151515;
  --sand:#ddd38e;
  --gold-hi:#efe08a;
  --gold-lo:#c7ad45;
  --gold-line:#e6d27a;
  --white:#ffffff;
  --text:#1e1e1e;
  --muted:#4a4a3a;
  --grey:#bdbdbd;
}
*{margin:0;padding:0;box-sizing:border-box}
html,body{width:1200px;height:2261px;overflow:hidden}
body{background:var(--sand);font-family:"Roboto",Arial,sans-serif;color:var(--text);position:relative}
.abs{position:absolute}
.bands{position:absolute;left:0;top:0}
/* header */
.logo{left:89px;top:38px;display:flex;align-items:center;gap:14px;color:var(--white);font-family:"Roboto",sans-serif;font-weight:500;font-size:30px;letter-spacing:1px}
.logo .mark{width:46px;height:46px;border:2px solid var(--white);border-radius:50%}
.nav{left:447px;top:54px;display:flex;gap:0;font-size:15px;color:var(--white);text-transform:uppercase}
.nav a{color:var(--white);text-decoration:none;position:absolute;white-space:nowrap}
.nav a.active{color:var(--gold-line);border-bottom:2px solid var(--gold-line);padding-bottom:4px}
.login{left:1029px;top:46px;width:82px;height:35px;border:1px solid var(--white);border-radius:3px;color:var(--white);font-size:15px;display:flex;align-items:center;justify-content:center}
/* hero */
.hero-title{left:89px;top:288px;font-family:"Oswald",sans-serif;font-weight:500;font-size:37px;color:var(--white)}
.hero-sub{left:89px;top:333px;font-family:"Oswald",sans-serif;font-weight:400;font-size:27px;color:var(--white)}
.cta{left:89px;top:396px;width:196px;height:58px;border-radius:4px;background:linear-gradient(var(--gold-hi),var(--gold-lo));border:2px solid #f3e8a8;font-size:23px;font-weight:500;color:#222;display:flex;align-items:center;justify-content:center}
.hero-art{left:560px;top:136px;width:530px;height:460px;border-radius:30px;background:radial-gradient(ellipse at center,#4a4038 0%,#2a2622 60%,rgba(28,28,28,0) 80%)}
.arrow{width:36px;height:36px;border-radius:50%;background:#2e2e2e;display:flex;align-items:center;justify-content:center}
/* services */
.h2{width:1200px;text-align:center;font-size:24px;font-weight:500;text-transform:uppercase}
.service{width:230px;text-align:center}
.service .icon{width:106px;height:106px;margin:0 auto;border-radius:50%;background:var(--white);box-shadow:0 0 0 4px rgba(255,255,255,.45),0 2px 6px rgba(0,0,0,.15);display:flex;align-items:center;justify-content:center}
.service h3{font-size:15.5px;font-weight:500;text-transform:uppercase;margin-top:28px;line-height:18px}
.service p{font-size:11px;line-height:17px;color:var(--muted);margin-top:10px}
.service .more{font-size:12.5px;margin-top:10px;color:#222}
/* events */
.events-title{color:var(--white)}
.events-lead{width:1200px;text-align:center;font-size:14px;font-weight:500;color:var(--white)}
.event{width:302px}
.event .pic{width:302px;height:180px;border-radius:6px}
.event h4{font-size:18px;font-weight:500;color:var(--white);margin-top:38px}
.event p{font-size:12px;line-height:21px;color:var(--white);margin-top:6px;padding-left:3px}
/* testimonials */
.avatar{width:94px;height:94px;border-radius:50%;border:4px solid var(--white)}
.quote{width:300px}
.quote p{font-size:12.5px;line-height:22px;color:var(--muted)}
.quote .name{font-size:11.5px;font-weight:700;margin-top:10px;color:#222}
.quote .role{font-size:12.5px;color:var(--muted);margin-top:6px}
.qmark{font-family:Georgia,serif;font-size:54px;line-height:1;color:#222}
/* footer */
.f-col{top:2015px;color:var(--white)}
.f-col h5{font-size:16px;font-weight:500;text-transform:uppercase;margin-bottom:24px}
.f-col p{font-size:11.5px;line-height:19px}
.links li{list-style:none;font-size:11.5px;line-height:24.5px}
.links li::before{content:"";display:inline-block;border-left:5px solid var(--white);border-top:4px solid transparent;border-bottom:4px solid transparent;margin-right:6px}
.signup{display:flex;margin-top:16px}
.signup .field{width:140px;height:31px;background:#e9e9e9;color:#777;font-size:11px;padding-left:14px;display:flex;align-items:center}
.signup .send{width:62px;height:31px;background:#1a1a1a;color:var(--white);font-size:12px;display:flex;align-items:center;justify-content:center}
.socials{display:flex;gap:14px;margin-top:20px}
.socials span{width:33px;height:33px;border:1.5px solid var(--white);border-radius:50%}
.copyright{width:1200px;top:2223px;left:-108px;text-align:center;font-size:12px;color:var(--white)}
</style>
</head>
<body>

<svg class="bands" width="1200" height="2261" viewBox="0 0 1200 2261" aria-hidden="true">
  <defs>
    <linearGradient id="eventsShade" x1="0" y1="0" x2="1" y2="1">
      <stop offset="0" stop-color="#141414"/>
      <stop offset=".5" stop-color="#1f1c18"/>
      <stop offset="1" stop-color="#0f0f0f"/>
    </linearGradient>
    <linearGradient id="footShade" x1="0" y1="0" x2="0" y2="1">
      <stop offset="0" stop-color="#2b2f31"/>
      <stop offset="1" stop-color="#1f2224"/>
    </linearGradient>
  </defs>
  <path d="M0 0H1200V565Q600 715 0 565Z" fill="#1c1c1c"/>
  <path d="M0 1123Q600 1041 1200 1123V1583Q600 1673 0 1583Z" fill="url(#eventsShade)"/>
  <path d="M0 1975Q600 1889 1200 1975V2261H0Z" fill="url(#footShade)"/>
  <rect x="0" y="2193" width="1200" height="68" fill="#151515"/>
</svg>

<!-- header -->
<div class="abs logo"><span>Velvet Crown</span><span class="mark"></span></div>
<nav class="abs nav">
  <a class="active" style="left:0">Home</a>
  <a style="left:80px">About us</a>
  <a style="left:188px">Services</a>
  <a style="left:294px">Projects</a>
  <a style="left:408px">Blog</a>
  <a style="left:483px">Contacts</a>
</nav>
<div class="abs login">LOGIN</div>

<!-- hero -->
<div class="abs hero-art" role="img" aria-label="Cartoon illustration of three young people in casual outfits"></div>
<h1 class="abs hero-title">VELVET CROWN IS A FULL SERVICE PR</h1>
<div class="abs hero-sub">Neque porro quisquam est qui dolorem ipsum</div>
<div class="abs cta">Get start Now</div>
<div class="abs arrow" style="left:32px;top:332px"><svg width="12" height="14" viewBox="0 0 12 14"><path d="M9 1L3 7l6 6" stroke="#fff" stroke-width="2" fill="none"/></svg></div>
<div class="abs arrow" style="left:1126px;top:332px"><svg width="12" height="14" viewBox="0 0 12 14"><path d="M3 1l6 6-6 6" stroke="#fff" stroke-width="2" fill="none"/></svg></div>

<!-- services -->
<h2 class="abs h2" style="top:695px">Our services are</h2>

<div class="abs service" style="left:81px;top:770px">
  <div class="icon"><svg width="30" height="32" viewBox="0 0 30 32"><circle cx="15" cy="9" r="8" fill="#111"/><path d="M1 32c0-10 6-13 14-13s14 3 14 13z" fill="#111"/></svg></div>
  <h3>PR Campaigns</h3>
  <p>Lorem Ipsum has been the industry's standard dummy text ever since the 1500s, when an unknown printer took a galley</p>
  <div class="more">Read More ▸</div>
</div>
<div class="abs service" style="left:346px;top:770px">
  <div class="icon"><svg width="38" height="36" viewBox="0 0 38 36"><path d="M37 1L1 15l11 4 3 13 5-8 9 6z" fill="#111"/><path d="M12 19L37 1 17 23" stroke="#fff" stroke-width="1.5" fill="none"/></svg></div>
  <h3>Media Relations</h3>
  <p>Lorem Ipsum has been the industry's standard dummy text ever since the 1500s, when an unknown printer took a galley</p>
  <div class="more">Read More ▸</div>
</div>
<div class="abs service" style="left:607px;top:770px">
  <div class="icon"><svg width="42" height="32" viewBox="0 0 42 32"><circle cx="9" cy="9" r="5" fill="#111"/><circle cx="33" cy="9" r="5" fill="#111"/><circle cx="21" cy="8" r="7" fill="#111"/><path d="M0 26c0-8 4-10 9-10s8 2 8 10z M25 26c0-8 3-10 8-10s9 2 9 10z" fill="#111"/><path d="M9 32c0-11 5-14 12-14s12 3 12 14z" fill="#111"/></svg></div>
  <h3>Talent Representation</h3>
  <p>Lorem Ipsum has been the industry's standard dummy text ever since the 1500s, when an unknown printer took a galley</p>
  <div class="more">Read More ▸</div>
</div>
<div class="abs service" style="left:871px;top:770px">
  <div class="icon"><svg width="44" height="40" viewBox="0 0 44 40"><circle cx="16" cy="24" r="10" fill="none" stroke="#111" stroke-width="7" stroke-dasharray="4 3"/><circle cx="16" cy="24" r="6" fill="none" stroke="#111" stroke-width="4"/><circle cx="34" cy="10" r="6" fill="none" stroke="#111" stroke-width="5" stroke-dasharray="3 2"/><circle cx="34" cy="30" r="5" fill="none" stroke="#111" stroke-width="4" stroke-dasharray="3 2"/></svg></div>
  <h3 style="margin-top:20px">Brand Marketing &amp;<br>Activations</h3>
  <p>Lorem Ipsum has been the industry's standard dummy text ever since the 1500s, when an unknown printer took a galley</p>
  <div class="more">Read More ▸</div>
</div>

<!-- special events -->
<h2 class="abs h2 events-title" style="top:1149px">Special events</h2>
<div class="abs events-lead" style="top:1197px">Lorem Ipsum is simply dummy text of the printing and typesetting industry</div>

<div class="abs event" style="left:87px;top:1251px">
  <div class="pic" role="img" aria-label="Photo of hands holding a phone with floating social icons" style="background:linear-gradient(135deg,#6f9fb8,#c7dbe3 50%,#7a8e6a)"></div>
  <h4>Neque porro quisquam est</h4>
  <p>Lorem Ipsum has been the industry's standard dummy text ever since the 1500s, when an unknown printer took</p>
</div>
<div class="abs event" style="left:444px;top:1251px">
  <div class="pic" role="img" aria-label="Photo of a group of young friends using devices at a table" style="background:linear-gradient(180deg,#d9dde0,#9a7a62 55%,#6b4a36)"></div>
  <h4>Neque porro quisquam est</h4>
  <p>Lorem Ipsum has been the industry's standard dummy text ever since the 1500s, when an unknown printer took</p>
</div>
<div class="abs event" style="left:806px;top:1251px">
  <div class="pic" role="img" aria-label="Photo of a hand touching a tablet screen" style="background:linear-gradient(135deg,#cfd4d8,#8f979e 50%,#3d444a)"></div>
  <h4>Neque porro quisquam est</h4>
  <p>Lorem Ipsum has been the industry's standard dummy text ever since the 1500s, when an unknown printer took</p>
</div>

<!-- testimonials -->
<h2 class="abs h2" style="top:1685px;font-weight:400">Testimonials</h2>

<div class="abs avatar" role="img" aria-label="Portrait of a smiling businessman" style="left:103px;top:1750px;background:linear-gradient(#d8c6b4,#6f8fb0)"></div>
<div class="abs qmark" style="left:207px;top:1745px">“</div>
<div class="abs quote" style="left:234px;top:1762px">
  <p>Lorem Ipsum has been the industry's standard dummy text ever since the 1500s, when an unknown printer took a galley of type and scrambled it to make</p>
  <div class="name">COLIN MARSH</div>
  <div class="role">Marketing Executive</div>
</div>
<div class="abs qmark" style="left:500px;top:1812px">”</div>

<div class="abs avatar" role="img" aria-label="Portrait of a smiling businesswoman" style="left:657px;top:1750px;background:linear-gradient(#e4d9cc,#8a6a4e)"></div>
<div class="abs qmark" style="left:763px;top:1745px">“</div>
<div class="abs quote" style="left:791px;top:1762px">
  <p>Lorem Ipsum has been the industry's standard dummy text ever since the 1500s, when an unknown printer took a galley of type and scrambled it to make</p>
  <div class="name">COLIN MARSH</div>
  <div class="role">Marketing Executive</div>
</div>
<div class="abs qmark" style="left:1058px;top:1812px">”</div>

<!-- footer -->
<div class="abs f-col" style="left:89px;width:232px">
  <h5>Text widget</h5>
  <p style="text-align:justify">Hostwell helps you to quickly and easily build incredible websites with PageForge.</p>
  <p style="text-align:justify;margin-top:19px">Proin gravida nibh vel velit auctor aliquet. Aenean sollicitudin, lorem quis bibendum auctor, nisi elit consequat ipsum, nec sagittis.</p>
</div>
<div class="abs f-col" style="left:436px">
  <h5>Links</h5>
  <ul class="links" style="margin-top:-4px">
    <li>Customer Support</li><li>Documentation</li><li>Resources</li><li>General FAQs</li><li>Shortcodes</li>
  </ul>
</div>
<div class="abs f-col" style="left:653px">
  <h5>Get in touch</h5>
  <p>Address : 1450 Harlow Ave,<br>Crestfield, NJ</p>
  <p style="margin-top:14px">Phone : 201 555 0148</p>
  <p style="margin-top:14px">Email : info@samplegate.com</p>
</div>
<div class="abs f-col" style="left:908px;width:210px">
  <h5>Newsletter</h5>
  <p style="margin-top:-6px">Your about us information would fit here nicely.</p>
  <div class="signup"><div class="field">Email address</div><div class="send">Submit</div></div>
  <div class="socials"><span></span><span></span><span></span></div>
</div>

<div class="abs copyright">Copyright © 2015. All Rights Reserved</div>

</body>
</html>
```